A flyer for future customers to get acquainted with our company

The flyer/card is intended for intermediaries. The purpose of this flyer is to introduce businesses to Dovrel.

It should convey: real estate and financing, with actual images. Various keywords describing what we do: project financing, temporary real estate financing, real estate financing, investment properties, transformations. We distinguish ourselves by being fast, flexible, and personal.

Please ensure the front has an attractive and inviting appearance, and leave space on the back for additional text.

Color codes: #E85B35 en #091E33

```html
<!DOCTYPE html>
<html lang="en">
<head>
<meta charset="utf-8">
<title>Dovrel – Real Estate and Financing Postcard</title>
<link rel="stylesheet" href="https://fonts.googleapis.com/css2?family=Bebas+Neue&family=Cabin:wght@400;600&family=Questrial&display=swap">
<style>
  :root {
    --orange: #E85B35;
    --navy: #091E33;
    --navy-mid: #13305a;
    --sky: #6f95cf;
    --white: #ffffff;
    --stamp: #d9d9d9;
    --backdrop: #e6e6e4;
  }
  * { margin: 0; padding: 0; box-sizing: border-box; }
  html, body { width: 1200px; height: 911px; overflow: hidden; background: var(--backdrop); }
  .stage { position: relative; width: 1200px; height: 911px; }

  .postcard {
    position: absolute;
    width: 567px; height: 378px;
    background: var(--white);
    overflow: hidden;
    box-shadow: 0 4px 14px rgba(0,0,0,.18);
  }
  .postcard > svg { position: absolute; inset: 0; width: 100%; height: 100%; }
  .postcard--back { left: 136px; top: 115px; }
  .postcard--front { left: 535px; top: 361px; }

  .brand {
    position: absolute;
    display: flex; align-items: center; gap: 5px;
    font-family: "Questrial", sans-serif;
    color: var(--navy);
    line-height: 1;
  }
  .brand__dot { border-radius: 50%; background: var(--orange); flex: none; }
  .postcard--back .brand { left: 348px; top: 16px; font-size: 27px; }
  .postcard--back .brand__dot { width: 9px; height: 9px; }
  .postcard--front .brand { left: 19px; top: 19px; font-size: 38px; }
  .postcard--front .brand__dot { width: 12px; height: 12px; }

  .stamp-box { position: absolute; left: 519px; top: 20px; width: 23px; height: 26px; background: var(--stamp); }

  .back-copy {
    position: absolute; left: 22px; top: 201px; width: 245px;
    font-family: "Cabin", sans-serif; font-size: 7.3px; line-height: 9.6px;
    color: var(--white);
  }
  .back-copy p + p { margin-top: 9.6px; }

  .contact-label {
    position: absolute; left: 22px; top: 302px; width: 252px;
    display: flex; align-items: center; gap: 18px;
    font-family: "Cabin", sans-serif; font-weight: 600; font-size: 9.5px; letter-spacing: .08em;
    color: var(--white);
  }
  .contact-label::before, .contact-label::after { content: ""; flex: 1; height: 1px; background: var(--orange); }

  .web-address {
    position: absolute;
    font-family: "Questrial", sans-serif; font-size: 18px; letter-spacing: .18em;
    color: var(--white); white-space: nowrap;
  }
  .web-address strong { color: var(--orange); font-weight: 400; }
  .postcard--back .web-address { left: 48px; top: 323px; }
  .postcard--front .web-address { left: 22px; top: 350px; }

  .headline {
    position: absolute; left: 19px; top: 68px;
    font-family: "Bebas Neue", sans-serif; font-size: 50px; line-height: 45px;
  }
  .headline__accent { color: var(--orange); display: block; }
  .headline__main { color: var(--navy); display: block; }

  .tagline {
    position: absolute; left: 19px; top: 168px; width: 200px;
    font-family: "Questrial", sans-serif; font-size: 19px; line-height: 23px;
    color: var(--orange);
  }

  .service-list {
    position: absolute; left: 19px; top: 225px;
    list-style: none;
    font-family: "Questrial", sans-serif; font-size: 10.8px; line-height: 17px;
    color: var(--navy);
    border-left: 1px solid var(--navy);
    margin-left: 4px; padding-left: 10px;
  }
  .service-list li { position: relative; }
  .service-list li::before {
    content: ""; position: absolute; left: -14px; top: 4.5px;
    width: 7px; height: 7px; border-radius: 50%; background: var(--navy);
  }
  .service-list li::after {
    content: ""; position: absolute; left: -12.3px; top: 6.2px;
    width: 3px; height: 1.6px; border-left: 1px solid var(--white); border-bottom: 1px solid var(--white);
    transform: rotate(-45deg);
  }
</style>
</head>
<body>
<main class="stage">

  <!-- Reverse side -->
  <section class="postcard postcard--back" aria-label="Postcard reverse">
    <svg viewBox="0 0 567 378" preserveAspectRatio="none">
      <defs>
        <linearGradient id="team-photo-fade" x1="0" y1="0" x2="0" y2="1">
          <stop offset="0" stop-color="#9fb0c8"/>
          <stop offset=".45" stop-color="#4d6387"/>
          <stop offset=".82" stop-color="var(--navy-mid)"/>
          <stop offset="1" stop-color="var(--navy-mid)"/>
        </linearGradient>
        <linearGradient id="meeting-photo" x1="0" y1="0" x2="1" y2="1">
          <stop offset="0" stop-color="#c9c2b8"/>
          <stop offset="1" stop-color="#5b5750"/>
        </linearGradient>
      </defs>
      <path class="back-panel" d="M0,0 H232 C310,70 300,250 254,378 H0 Z" fill="url(#team-photo-fade)" role="img" aria-label="Photo of business people shaking hands and applauding in an office, fading into navy"/>
      <path class="back-panel-base" d="M0,190 H296 C292,260 275,320 254,378 H0 Z" fill="var(--navy-mid)" opacity=".0"/>
      <path class="accent-swoosh" d="M283,140 C300,220 288,300 254,378 H296 C318,300 316,220 283,140 Z" fill="var(--orange)"/>
      <path d="M232,0 C250,14 262,28 270,44" stroke="var(--orange)" stroke-width="1" fill="none"/>
      <circle cx="290" cy="83" r="62" fill="var(--white)"/>
      <circle cx="290" cy="83" r="60" fill="url(#meeting-photo)" role="img" aria-label="Photo of a couple signing papers beside a small house model"/>
    </svg>

    <div class="brand"><span class="brand__name">Dovrel</span><span class="brand__dot"></span></div>
    <div class="stamp-box" aria-label="Stamp area"></div>

    <div class="back-copy">
      <p>Lorem ipsum dolor sit amet, consectetur adipiscing elit, sed do eiusmod tempor incididunt ut labore et dolore magna aliqua. Quis ipsum suspendisse ultrices gravida. Risus commodo viverra maecenas accumsan lacus vel facilisis.</p>
      <p>Lorem ipsum dolor sit amet, consectetur adipiscing elit, sed do eiusmod tempor incididunt ut labore et dolore magna aliqua. Quis ipsum suspendisse ultrices gravida. Risus commodo viverra maecenas accumsan lacus vel facilisis.</p>
    </div>
    <div class="contact-label">CONTACT US</div>
    <div class="web-address">www.<strong>dovrel</strong>.com</div>
  </section>

  <!-- Front side -->
  <section class="postcard postcard--front" aria-label="Postcard front">
    <svg viewBox="0 0 567 378" preserveAspectRatio="none">
      <defs>
        <linearGradient id="tower-photo" x1="0" y1="0" x2="0" y2="1">
          <stop offset="0" stop-color="#b9cbe6"/>
          <stop offset=".4" stop-color="var(--sky)"/>
          <stop offset=".75" stop-color="#2b4f92"/>
          <stop offset="1" stop-color="#16356f"/>
        </linearGradient>
      </defs>
      <path class="hero-photo" d="M398,0 H567 V378 H276 C296,225 332,105 398,0 Z" fill="url(#tower-photo)" role="img" aria-label="Photo of a glass skyscraper rising above a glowing blue financial chart"/>
      <path class="accent-swoosh" d="M392,4 C338,72 256,230 229,378 H270 C289,228 328,110 392,4 Z" fill="var(--orange)"/>
      <path class="base-band" d="M0,334 C90,352 172,340 238,292 L229,378 H0 Z" fill="var(--navy)"/>
      <path class="base-stripe" d="M0,314 C90,342 180,326 246,270 L240,288 C172,336 90,350 0,331 Z" fill="var(--orange)"/>
    </svg>

    <div class="brand"><span class="brand__name">Dovrel</span><span class="brand__dot"></span></div>

    <h1 class="headline">
      <span class="headline__accent">REAL ESTATE</span>
      <span class="headline__main">AND FINANCING</span>
    </h1>
    <p class="tagline">FAST, FLEXIBLE, AND PERSONAL.</p>

    <ul class="service-list">
      <li>Project Financing,</li>
      <li>Temporary Real estate Financing,</li>
      <li>Real estate Financing,</li>
      <li>Investment Properties,</li>
      <li>Transformations</li>
    </ul>

    <div class="web-address">www.<strong>dovrel</strong>.com</div>
  </section>

</main>
</body>
</html>
```